Plum Meadow Label

Design a label for new brand called Plum Meadow. The specific product label :
Plum Meadow Cocoa Butter Lotion. You only need to design the front label.
I have included the logo and a bottle jpeg with 2 bottles on it. Please try your best.

Industry/Entity Type

Product

Requirements
Must have
• text on the label other than the logo:
cocoa butter
lotion
8.5oz/250ml

Original Moisturizing Formula
Smoothes Marks
Protect Skin

__________________________________
- ALTERNATIVE TEXT TO ALSO USE:
Smoothes Dry Skin, Blemishes & Stretch Marks
Softens Hands, Face and Body
Vitamin E

```html
<!DOCTYPE html>
<html lang="en">
<head>
<meta charset="utf-8">
<title>Plum Meadow Cocoa Butter Lotion – Front Label</title>
<link rel="stylesheet" href="https://fonts.googleapis.com/css2?family=Nunito:wght@800&family=Courgette&family=EB+Garamond:ital,wght@1,500&display=swap">
<style>
  :root {
    --page: #f3f1ec;
    --label-pink: #f6bdd2;
    --brand-pink: #e0136f;
    --cocoa: #5a1631;
    --teal: #35b4c6;
    --sage-border: #6d8c69;
    --sage-fill: #d6efd6;
    --ink: #1d1a1b;
    --flourish: rgba(255, 255, 255, 0.55);
  }
  * { box-sizing: border-box; margin: 0; padding: 0; }
  html, body {
    width: 695px; height: 1200px; overflow: hidden;
    background: var(--page);
  }
  .label {
    position: absolute;
    left: 45px; top: 100px;
    width: 605px; height: 1000px;
    background: var(--label-pink);
    border-radius: 46px;
    text-align: center;
  }
  .ingredients-art {
    position: absolute;
    left: 115px; top: 40px;
    width: 380px; height: 300px;
    border-radius: 44% 48% 40% 46%;
    background:
      radial-gradient(circle at 22% 30%, #8a6cc4 0 22%, transparent 40%),
      radial-gradient(circle at 42% 55%, #f1c21b 0 18%, transparent 34%),
      radial-gradient(circle at 74% 36%, #5b3524 0 24%, transparent 42%),
      radial-gradient(circle at 70% 70%, #8d6a4c 0 14%, transparent 30%),
      linear-gradient(135deg, #b9a3de, #f2d36b 50%, #7a5036);
    opacity: 0.9;
  }
  .flourish {
    position: absolute;
    left: 90px; top: 355px;
    width: 425px; height: 110px;
    border-radius: 50%;
    background: radial-gradient(ellipse at center, var(--flourish), transparent 70%);
  }
  .brand-name {
    position: absolute;
    left: 0; right: 0; top: 415px;
    font-family: "Nunito", sans-serif;
    font-weight: 800;
    font-size: 78px;
    line-height: 1;
    color: var(--brand-pink);
  }
  .product-name {
    position: absolute;
    left: 0; right: 0; top: 520px;
    font-family: "Nunito", sans-serif;
    font-weight: 800;
    font-size: 46px;
    line-height: 1;
    color: var(--cocoa);
  }
  .product-type {
    position: absolute;
    left: 0; right: 0; top: 574px;
    font-family: "Nunito", sans-serif;
    font-weight: 800;
    font-size: 33px;
    line-height: 1;
    color: var(--teal);
  }
  .formula-box {
    position: absolute;
    left: 40px; top: 640px;
    width: 525px; height: 64px;
    border: 4px solid var(--sage-border);
    border-radius: 14px;
    background: var(--sage-fill);
    display: flex; align-items: center; justify-content: center;
    font-family: "Courgette", cursive;
    font-size: 27px;
    color: var(--brand-pink);
  }
  .benefits {
    position: absolute;
    left: 0; right: 0; top: 735px;
    list-style: none;
    font-family: "EB Garamond", serif;
    font-style: italic;
    font-weight: 500;
    font-size: 24px;
    line-height: 34px;
    color: var(--ink);
  }
  .net-volume {
    position: absolute;
    left: 0; right: 0; top: 920px;
    font-family: "EB Garamond", serif;
    font-size: 19px;
    color: var(--brand-pink);
  }
</style>
</head>
<body>
  <section class="label">
    <div class="ingredients-art" role="img" aria-label="Illustration of lavender, sunflowers, a split coconut and shea nuts"></div>
    <div class="flourish" role="img" aria-label="Decorative white swirl flourish"></div>
    <h1 class="brand-name">Plum Meadow</h1>
    <p class="product-name">Cocoa Butter</p>
    <p class="product-type">Face and Body Lotion</p>
    <div class="formula-box">Original Moisturizing Formula with Vitamin E</div>
    <ul class="benefits">
      <li>Smoothes Dry Skin</li>
      <li>Removes Blemishes &amp; Stretch Marks</li>
      <li>Softens Hands, Face and Body</li>
      <li>Protects the skin without harmful chemicals</li>
    </ul>
    <p class="net-volume">8.5oz/250ml</p>
  </section>
</body>
</html>
```